■レイアウトの希望について
◎2カラムで、必要に応じて上ナビも入れてください。
※全体の左右を970pxで、ナビの左右サイズを300pxでお願いします。
◎写真やイラストなどのイメージ画像は、最低1点以上入れてください。(有料画像も可)
※現サイトのイラストは自由に使用ください。

■内容について
◎サイト名のロゴは現行のものでなく新たにご提案ください。
※フォントを使用したものでOKです。
◎ヘッダーはスマホサイズになった場合のことも考えて作成してください。
※サイト名の周りは適当にキャッチを入れていただくか、文字を○○○○の形で入れてもかまいません。
◎トップページに入れる文章はできていますが、文字数が少ないのでバランスが悪ければ○○○○の形でプラスしてください。
◎ナビに入れるタイトルはページ構成から抜き出して入れてください。
※上ナビも入れる場合は項目をご提案ください。(左右ナビと変えてもダブってもOK)
※新聞奨学金を目立たせたいので、ナビを工夫されても良いかと思われます。
◎文章とページ構成は以下からダウンロードしてください。
http://www.qx5.co.jp/rmt.zip
基本的にはお任せですが、派手な色やくすんだ色は避けてください。(バランスの良い、落ち着いた色が希望)
納品ファイルは、JPG形式 (.jpg)またはPNG形式 (.png)のいずれかひとつと、イラストレーター形式 (.ai) またはフォトショップ形式 (.psd) のいずれかひとつの、計2ファイルに変更させていただきます。
申し訳ございませんが、ご了承ください。
提案の締め切り日を2日間延ばして6月20日にしました。

第一希望の新聞奨学金ページへの誘導方法がうまく、その他のアイデアも多くいただきました。
それに加え、全体のバランスや色使いが好みだったので、決めさせていただきました。
また、修正依頼などもすぐに対応いただき、助かりました。

多くのご提案をいただき、ありがとうございました。
結局は主観的な好みで決めさせていただきましたが、迷ったご提案も数点ありました。
なお、締切日ギリギリのご提案は、修正依頼が出せないので、良いご提案も見送らせていただいたものもありました。

```html
<!DOCTYPE html>
<html lang="ja">
<head>
<meta charset="utf-8">
<title>学費ナビ</title>
<link rel="stylesheet" href="https://fonts.googleapis.com/css2?family=Noto+Sans+JP:wght@400;500;700;900&display=swap">
<style>
:root{
  --blue:#1a86c8;
  --blue-dark:#1d5d9b;
  --navy:#17457a;
  --sky:#e6f3fb;
  --sky-line:#b9dcf1;
  --text:#333;
  --muted:#666;
  --line:#d9e4ec;
  --accent:#d0452d;
  --white:#fff;
  --footer:#1a86c8;
}
*{box-sizing:border-box;margin:0;padding:0}
html,body{width:1200px;height:2668px;overflow:hidden}
body{background:var(--white);font-family:"Noto Sans JP",sans-serif;color:var(--text);font-size:15px;line-height:1.7;position:relative}
a{color:inherit;text-decoration:none}
.wrap{position:absolute;left:30px;width:1140px}

/* header */
.site-header{top:0;height:92px;display:flex;align-items:center;justify-content:space-between}
.brand{display:flex;flex-direction:column}
.brand-tag{font-size:13px;color:var(--muted)}
.brand-name{font-size:30px;font-weight:700;color:var(--text);line-height:1.2}
.header-right{display:flex;align-items:center;gap:22px;font-size:14px}
.header-link::before{content:"▶";color:var(--blue);font-size:10px;margin-right:6px}
.request-btn{background:var(--blue-dark);color:var(--white);padding:10px 22px;border-radius:4px;font-weight:700;font-size:20px;line-height:1.2}
.request-btn small{display:block;font-size:11px;font-weight:400}

/* sidebar */
.sidebar{position:absolute;left:30px;top:108px;width:250px}
.side-nav{list-style:none;border-top:1px solid var(--line)}
.side-nav li{height:56px;border-bottom:1px solid var(--line);display:flex;align-items:center;gap:12px;padding-left:12px;font-size:17px;font-weight:500}
.side-nav .ico{width:18px;height:18px;background:var(--blue);border-radius:3px}
.side-nav li.contact{height:110px;background:var(--blue);color:var(--white);flex-direction:column;align-items:flex-start;justify-content:center;padding:0 14px;gap:6px}
.side-nav li.contact strong{font-size:19px}
.side-nav li.contact span{background:var(--white);color:var(--blue);font-size:12px;padding:4px 8px;line-height:1.4}
.info-title{margin-top:30px;font-size:22px;font-weight:900;color:var(--blue-dark);border-bottom:3px solid var(--blue);padding-bottom:4px}
.info-list{list-style:none}
.info-list li{display:flex;align-items:center;gap:10px;font-size:12px;border-bottom:1px dotted var(--line);padding:10px 0;white-space:nowrap}
.info-list .date{background:var(--blue);color:var(--white);padding:2px 6px;font-size:12px;flex:none}

/* main */
.main{position:absolute;left:300px;top:96px;width:870px}
.hero{height:470px;background:var(--sky);border:1px solid var(--sky-line);position:relative;overflow:hidden}
.hero-photo{position:absolute;right:0;top:0;width:520px;height:100%;background:linear-gradient(120deg,#dfeef8,#f6efe6 55%,#e9dfd2)}
.hero-copy{position:absolute;left:20px;top:44px;width:580px;text-align:center}
.hero-copy .lead{display:inline-block;border:1px solid var(--blue);color:var(--blue);background:var(--white);padding:2px 18px;font-size:16px}
.hero-copy h1{font-size:38px;color:var(--blue-dark);font-weight:900;margin-top:12px;line-height:1.3;white-space:nowrap}
.hero-copy p{font-size:26px;color:var(--blue-dark);font-weight:700}

.intro{display:flex;gap:20px;margin-top:26px}
.intro p{flex:1;font-size:14px}
.intro p em{font-style:normal;color:var(--accent)}
.intro-box{width:280px;align-self:flex-start;border:1px solid var(--blue);padding:10px 14px;font-size:13px;color:var(--blue-dark)}
.intro-box li{list-style:none}
.intro-box li::before{content:"● ";color:var(--blue)}

.paper{margin-top:26px;border:2px solid var(--blue);height:240px;padding:18px 24px;position:relative}
.paper h2{font-size:26px;font-weight:900;color:var(--blue-dark);display:flex;align-items:center;gap:10px;border-bottom:1px solid var(--sky-line);padding-bottom:8px}
.paper h2 .badge{width:34px;height:34px;background:var(--blue);color:var(--white);display:flex;align-items:center;justify-content:center;font-size:20px}
.paper p{font-size:13px;margin-top:10px;width:560px}
.more-btn{position:absolute;right:24px;bottom:20px;background:var(--blue);color:var(--white);padding:8px 24px;font-size:15px;font-weight:700;border-radius:3px}

.types-title{margin-top:24px;background:var(--blue);color:var(--white);text-align:center;font-size:22px;font-weight:700;height:44px;line-height:44px}
.types{display:flex;gap:14px;margin-top:12px}
.type{flex:1;border:2px solid var(--blue);height:130px;text-align:center;padding-top:14px}
.type h3{font-size:26px;font-weight:900;color:var(--blue-dark)}
.type h3 small{font-size:16px}
.type p{font-size:13px;color:var(--muted);margin-top:8px}

.cards{display:grid;grid-template-columns:1fr 1fr;gap:20px 24px;margin-top:26px}
.card-photo{height:320px;position:relative}
.card-photo .ph{position:absolute;inset:0}
.card-photo h3{position:absolute;left:20px;top:24px;font-size:28px;font-weight:900;color:var(--white);text-shadow:0 1px 4px rgba(0,0,0,.35)}
.card-photo.boxed h3{background:rgba(255,255,255,.9);color:var(--blue-dark);text-shadow:none;padding:4px 14px}
.card-text{font-size:13px;height:200px;padding-top:14px;position:relative}
.card-text em{font-style:normal;color:var(--accent)}
.card-text .go{position:absolute;left:0;bottom:14px;color:var(--blue);font-size:13px}
.card-text .go::before{content:"▶ "}

.cta{display:flex;gap:24px;margin-top:28px}
.cta a{flex:1;height:120px;border:2px solid var(--blue);background:var(--sky);display:flex;flex-direction:column;align-items:center;justify-content:center;color:var(--blue-dark)}
.cta small{font-size:14px}
.cta strong{font-size:28px;font-weight:900}

.page-top{position:absolute;right:30px;top:2526px;background:var(--blue);color:var(--white);font-size:14px;padding:6px 30px}
.site-footer{position:absolute;left:0;top:2568px;width:1200px;height:62px;background:var(--footer);color:var(--white);display:flex;align-items:center;gap:44px;padding-left:40px;font-size:15px}
.site-footer a::before{content:"▶ ";font-size:10px}
.copyright{position:absolute;left:0;top:2636px;width:1200px;text-align:center;font-size:12px;color:var(--muted)}
</style>
</head>
<body>
<header class="wrap site-header">
  <div class="brand">
    <span class="brand-tag">奨学金情報サイト</span>
    <span class="brand-name">学費ナビ</span>
  </div>
  <div class="header-right">
    <a class="header-link" href="#">よくある質問</a>
    <a class="header-link" href="#">運営者について</a>
    <a class="request-btn" href="#">資料請求する<small>新聞奨学会のパンフレットを無料でお届け</small></a>
  </div>
</header>

<aside class="sidebar">
  <ul class="side-nav">
    <li><span class="ico"></span>奨学金とは?</li>
    <li><span class="ico"></span>奨学金の種類</li>
    <li><span class="ico"></span>新聞奨学金</li>
    <li><span class="ico"></span>奨学金の借り方</li>
    <li><span class="ico"></span>奨学金の返済方法</li>
    <li class="contact"><strong>お問い合わせフォーム</strong><span>奨学金について何でもお気軽に</span></li>
    <li><span class="ico"></span>よくある質問</li>
    <li><span class="ico"></span>リンク集</li>
  </ul>
  <h2 class="info-title">INFOMATION</h2>
  <ul class="info-list">
    <li><span class="date">2015.4.17</span>サイトリニューアルしました。</li>
    <li><span class="date">2015.4.17</span>サイトリニューアルしました。</li>
    <li><span class="date">2015.4.17</span>サイトリニューアルしました。</li>
    <li><span class="date">2015.4.17</span>サイトリニューアルしました。</li>
    <li><span class="date">2015.4.17</span>サイトリニューアルしました。</li>
    <li><span class="date">2015.4.17</span>サイトリニューアルしました。</li>
  </ul>
</aside>

<main class="main">
  <section class="hero">
    <div class="hero-photo" role="img" aria-label="机で勉強する学生の写真"></div>
    <div class="hero-copy">
      <span class="lead">奨学金について詳しく解説!</span>
      <h1>奨学金を知って、上手に活用!</h1>
      <p>自分にあったプランを探しましょう!</p>
    </div>
  </section>

  <section class="intro">
    <p>「奨学金」とは、経済的な理由で進学が困難な学生のための制度です。<em>「進学を諦めない」</em>ために、それぞれの制度の特徴を知ることが大切です。高校や専門学校・大学・大学院・海外の学校に進学するための、さまざまな奨学金の情報を掲載しています。自分に合ったプランを見つけましょう。</p>
    <ul class="intro-box">
      <li>学費の不安を解消したい方</li>
      <li>奨学金の種類を知りたい方</li>
      <li>働きながら学びたい方</li>
    </ul>
  </section>

  <section class="paper">
    <h2><span class="badge">!</span>働きながら学費を賄われる、新聞奨学会</h2>
    <p>新聞販売所で働きながら学費の支援を受けられる制度です。住まいや食事の補助もあり、卒業時には返済の必要がないため、多くの学生が利用しています。仕事と学業を両立しながら、自立した学生生活を送ることができます。</p>
    <a class="more-btn" href="#">新聞奨学金をさらに詳しく</a>
  </section>

  <h2 class="types-title">3種類の奨学金</h2>
  <div class="types">
    <div class="type"><h3>借りる<small>「貸与型」</small></h3><p>卒業後に返済する奨学金</p></div>
    <div class="type"><h3>稼ぐ<small>「新聞」</small></h3><p>働きながら学費を得る奨学金</p></div>
    <div class="type"><h3>もらう<small>「給付型」</small></h3><p>返済不要の奨学金</p></div>
  </div>

  <div class="cards">
    <div class="card-photo"><div class="ph" role="img" aria-label="積み重ねた本の写真" style="background:linear-gradient(135deg,#c9a27a,#8a5d3b)"></div><h3>奨学金制度のしくみ</h3></div>
    <div class="card-photo boxed"><div class="ph" role="img" aria-label="書類を記入する手元の写真" style="background:linear-gradient(135deg,#eef0f2,#c9cdd2)"></div><h3>給付方法に二種類</h3></div>
    <div class="card-text">奨学金には、国や地方自治体、学校や民間団体など様々な運営主体があります。それぞれに条件や金額が異なるため、<em>自分に合った制度を比較すること</em>が大切です。<a class="go" href="#">さらに詳しく</a></div>
    <div class="card-text">奨学金は、大きく分けて二つの給付方法があります。返済が必要な「貸与型」と、返済が不要な「給付型」です。<em>条件をよく確認しましょう。</em><a class="go" href="#">さらに詳しく</a></div>
    <div class="card-photo boxed"><div class="ph" role="img" aria-label="ノートとペンの写真" style="background:linear-gradient(135deg,#f3f3f1,#c7c9cc)"></div><h3>奨学金を受けるには?</h3></div>
    <div class="card-photo"><div class="ph" role="img" aria-label="キーボードを操作する手元の写真" style="background:linear-gradient(135deg,#5d5f63,#2e3033)"></div><h3>奨学金の返済</h3></div>
    <div class="card-text">まずは、<em>自分の目的に合う奨学金を探すこと</em>から始めましょう。申込の時期や必要書類は制度によって異なります。早めの準備が大切です。<a class="go" href="#">さらに詳しく</a></div>
    <div class="card-text">貸与型の奨学金は、卒業後に毎月返済していきます。返済が難しい場合は、猶予や減額の制度もあるので確認しておきましょう。<a class="go" href="#">さらに詳しく</a></div>
  </div>

  <div class="cta">
    <a href="#"><small>ご質問・お問い合わせはこちら</small><strong>お問い合わせフォーム</strong></a>
    <a href="#"><small>無料パンフレットのご請求はこちら</small><strong>資料請求する</strong></a>
  </div>
</main>

<a class="page-top" href="#">▲ Page Top</a>
<footer class="site-footer">
  <a href="#">よくある質問</a><a href="#">リンク集</a><a href="#">お問い合わせ</a><a href="#">運営者について</a><a href="#">サイトマップ</a>
</footer>
<p class="copyright">Copyright (c) 2015 学費ナビ All Rights Reserved.</p>
</body>
</html>
```